Portfolio site - Need a basic WordPress or SquareSpace site

I need a portfolio site where I have the option to keep updating it on my own. Therefore, I'm guessing I need one that uses WordPress or SquareSpace. I just need a simple and elegant design. I'm a writer (scholarly, fiction and journalism).

Target Market(s)

Adult

Industry/Entity Type

Writer

Number of Pages Required

4 page

Font styles to use
Serif

Colors
b7a5cd
e667a6
85abd2

Requirements
Must have
• Easily updatable features. I'll have to publish links and small blurbs from time to time. And maybe the occasional image.
• Pages should be:
• Home
• Work
• Press
• Contact

```html
<!DOCTYPE html>
<html lang="en">
<head>
<meta charset="utf-8">
<title>Mirela Vantos — Writer</title>
<link href="https://fonts.googleapis.com/css2?family=Karla:wght@400;700;800&family=Merriweather:ital,wght@0,300;0,400;1,400&display=swap" rel="stylesheet">
<style>
:root{
  --backdrop:#e3e4e6;
  --paper:#ffffff;
  --ink:#1d1d1f;
  --muted:#555a60;
  --rule:#cfcfd2;
  --rule-strong:#2a2a2d;
  --lavender:#b7a5cd;
  --rose:#e667a6;
  --sky:#85abd2;
  --photo-brick:#8a4a3e;
  --photo-paper:#d9cfc2;
  --photo-green:#86b0a3;
  --photo-grey:#b9bcbf;
  --photo-food:#c9b59a;
}
*{box-sizing:border-box;margin:0;padding:0}
html,body{width:1010px;height:1200px;overflow:hidden;background:var(--backdrop)}
body{font-family:"Merriweather",Georgia,serif;color:var(--ink)}
.page{position:absolute;left:224px;top:0;width:562px;height:1200px;background:var(--paper);box-shadow:0 0 6px rgba(0,0,0,.12)}
.abs{position:absolute}
.topbar .menu{left:35px;top:4px}
.topbar .social{top:5px;width:8px;height:8px;border-radius:50%;background:var(--ink)}
.logo{left:0;width:100%;top:28px;text-align:center;font-size:12px;letter-spacing:.5px}
.nav{top:62px;left:0;width:100%;display:flex;justify-content:center;gap:16px;font-family:"Karla",sans-serif;font-weight:800;font-size:5.5px;letter-spacing:.5px;text-transform:uppercase}
.nav .current{color:var(--rose)}
.photo{position:absolute}
.hero{left:0;top:78px;width:562px;height:207px;background:linear-gradient(100deg,var(--photo-brick) 0%,#a56a5a 45%,#4b4540 75%,#2b2a28 100%)}
.tags{display:flex;gap:3px}
.tag{background:var(--sky);color:#fff;font-family:"Karla",sans-serif;font-weight:700;font-size:4px;padding:1px 3px;text-transform:uppercase;letter-spacing:.4px}
.overlay-title{font-family:"Karla",sans-serif;font-weight:800;color:#fff;line-height:23.5px}
.meta{font-family:"Karla",sans-serif;font-weight:700;font-size:4px;letter-spacing:.4px;text-transform:uppercase}
.light{color:#fff}
.arrows{color:#fff;font-size:9px;font-family:"Karla",sans-serif}
.section-head{left:35px;width:492px;border-top:2px solid var(--rule-strong);border-bottom:1px solid var(--rule)}
.section-head h2{font-family:"Karla",sans-serif;font-weight:800;font-size:12.5px;position:absolute;left:0}
.see-all{position:absolute;right:0;font-family:"Karla",sans-serif;font-weight:800;font-size:5px;letter-spacing:.8px}
.lead-title{left:35px;top:540px;width:324px;font-family:"Karla",sans-serif;font-weight:800;font-size:17.5px;line-height:20px}
.lead-excerpt{left:35px;top:589px;width:324px;font-size:12.2px;line-height:15.6px;font-weight:300;color:#333}
.cat{font-family:"Karla",sans-serif;font-weight:700;font-size:3.8px;letter-spacing:.4px;text-transform:uppercase;color:var(--muted)}
.card-title{font-family:"Karla",sans-serif;font-weight:800;font-size:10px;line-height:12px}
.mini-title{font-family:"Karla",sans-serif;font-weight:800;font-size:5.2px;line-height:6.4px}
.hr{height:1px;background:var(--rule)}
.hr.dark{height:2px;background:#999}
.post-date{left:35px;font-family:"Karla",sans-serif;font-weight:700;font-size:3.8px;text-transform:uppercase}
.post-title{font-family:"Karla",sans-serif;font-weight:800;font-size:9.6px;line-height:11.6px}
.post-excerpt{font-size:6.1px;line-height:9.4px;color:#444;width:148px}
.side-head{font-family:"Karla",sans-serif;font-weight:800;font-size:5.2px}
.side-list{font-size:6.1px;line-height:9.4px;color:#333;width:156px}
.ad{left:371px;top:693px;width:156px;height:83px;background:#b3dedb;overflow:hidden}
.ad-art{position:absolute;left:0;top:0;width:100px;height:83px;background:linear-gradient(160deg,#6fc5bf 0%,#e5e1c8 30%,#e0433a 50%,#5a1f14 72%,#f36b4c 100%)}
.ad-text{position:absolute;left:110px;top:27px;width:42px;text-align:center;font-family:"Karla",sans-serif;font-size:8.5px;line-height:10px;color:#3d4b4f}
.ad-sub{font-size:3px;display:block;margin-top:3px}
.follow{left:371px;top:963px;width:156px;height:109px;border:1.5px solid #bbb}
.follow h3{position:absolute;top:10px;width:100%;text-align:center;font-family:"Karla",sans-serif;font-weight:800;font-size:4.5px;letter-spacing:.6px;text-transform:uppercase}
.follow p{position:absolute;left:12px;top:23px;width:134px;font-size:11px;line-height:14.6px;font-weight:300}
.follow .field{position:absolute;left:12px;top:76px;width:79px;height:22px;border:1px solid #ddd;font-size:4.4px;color:#999;padding:8px 5px;white-space:nowrap;overflow:hidden}
.follow .btn{position:absolute;left:94px;top:76px;width:50px;height:22px;background:var(--rose);color:#fff;font-family:"Karla",sans-serif;font-weight:800;font-size:4.5px;letter-spacing:.7px;text-align:center;line-height:22px}
.feature{left:0;top:1000px;width:359px;height:200px;background:linear-gradient(160deg,#b7a08a 0%,var(--photo-food) 30%,#e9e4dc 55%,#5d7b8c 85%,#3e5566 100%)}
</style>
</head>
<body>
<div class="page">
  <header class="topbar">
    <svg class="abs menu" width="10" height="9" viewBox="0 0 10 9"><rect y="0" width="10" height="1.6" fill="#1d1d1f"/><rect y="3.6" width="10" height="1.6" fill="#1d1d1f"/><rect y="7.2" width="10" height="1.6" fill="#1d1d1f"/></svg>
    <svg class="abs" style="left:60px;top:4px" width="9" height="9" viewBox="0 0 9 9"><circle cx="3.6" cy="3.6" r="2.7" fill="none" stroke="#1d1d1f" stroke-width="1.2"/><line x1="5.6" y1="5.6" x2="8.4" y2="8.4" stroke="#1d1d1f" stroke-width="1.4"/></svg>
    <span class="abs social" style="left:475px"></span>
    <span class="abs social" style="left:495px"></span>
    <span class="abs social" style="left:515px"></span>
    <div class="abs logo">Mirela Vantos</div>
    <nav class="abs nav"><span class="current">Home</span><span>Work ▾</span><span>Press ▾</span><span>Contact</span></nav>
  </header>

  <section>
    <div class="photo hero" role="img" aria-label="Woman reading on a bed in front of a herringbone brick wall"></div>
    <div class="abs tags" style="left:35px;top:195px"><span class="tag">Learning</span><span class="tag">Travel</span></div>
    <h1 class="abs overlay-title" style="left:35px;top:206px;width:340px;font-size:22px">Let’s Appreciate the Little Things in Our Life</h1>
    <div class="abs meta light" style="left:35px;top:266px">By Clara Weston / Aug 23, 2015 / 8</div>
    <div class="abs arrows" style="left:530px;top:268px">‹&nbsp;&nbsp;&nbsp;&nbsp;›</div>
  </section>

  <section>
    <div class="abs section-head" style="top:308px;height:31px"><h2 style="top:5px">Top Stories</h2><span class="see-all" style="top:12px">SEE ALL POSTS →</span></div>
    <div class="photo" style="left:35px;top:346px;width:324px;height:182px;background:linear-gradient(120deg,#b98e5e 0%,var(--photo-paper) 35%,#eeeae3 70%,#c7a27a 100%)" role="img" aria-label="Hand pointing at leaf sketches in an open book"></div>
    <div class="abs tags" style="left:43px;top:353px"><span class="tag">Learning</span><span class="tag">Stories</span></div>
    <h2 class="abs lead-title">How To Find More Inspiration In Reading and Writing</h2>
    <p class="abs lead-excerpt">Books and magazines are just the best. I love everything related to books and magazines, the smell, being able to... Continue Reading</p>
    <div class="abs meta" style="left:35px;top:651px">By Clara Weston / Aug 3, 2015</div>

    <div class="photo" style="left:371px;top:346px;width:156px;height:88px;background:radial-gradient(circle at 50% 50%,#a9cbbd 0%,var(--photo-green) 50%,#4d6f63 100%)" role="img" aria-label="Close-up of a succulent plant"></div>
    <div class="abs cat" style="left:371px;top:439px">Learning / Photography</div>
    <h3 class="abs card-title" style="left:371px;top:447px;width:140px">Learn More About Nature and Photography</h3>
    <div class="abs hr dark" style="left:371px;top:484px;width:156px"></div>

    <div class="photo" style="left:371px;top:493px;width:75px;height:42px;background:linear-gradient(180deg,#e8e8e8,#c9c7c2)" role="img" aria-label="Person working at a desk in a bright room"></div>
    <div class="photo" style="left:453px;top:493px;width:74px;height:42px;background:linear-gradient(180deg,#8d9aa0,#6a7560 60%,#9aa0a3)" role="img" aria-label="Road winding through hills"></div>
    <div class="abs cat" style="left:371px;top:541px">Society / Stories</div>
    <div class="abs cat" style="left:453px;top:541px">Stories / Travel</div>
    <h4 class="abs mini-title" style="left:371px;top:549px;width:48px">The Remote Working Lifestyle</h4>
    <h4 class="abs mini-title" style="left:453px;top:549px;width:62px">Exploring Beautiful New Zealand</h4>
    <div class="abs hr dark" style="left:371px;top:575px;width:75px"></div>
    <div class="abs hr dark" style="left:453px;top:575px;width:74px"></div>

    <div class="photo" style="left:371px;top:585px;width:75px;height:41px;background:linear-gradient(140deg,#8b6a4e,#e6dccd 50%,#a07a55)" role="img" aria-label="Bowl of pumpkin soup"></div>
    <div class="photo" style="left:453px;top:585px;width:74px;height:41px;background:linear-gradient(180deg,#e9e9e9,#bdbdbd 55%,var(--photo-grey))" role="img" aria-label="Figure on a misty beach"></div>
    <div class="abs cat" style="left:371px;top:632px">Food / Stories</div>
    <div class="abs cat" style="left:453px;top:632px">Nature / Stories</div>
    <h4 class="abs mini-title" style="left:371px;top:640px;width:72px">The Best Pumpkin Soup for Cold Winter Days</h4>
    <h4 class="abs mini-title" style="left:453px;top:640px;width:52px">A Weekend Trip to the Coast</h4>
  </section>

  <section>
    <div class="abs section-head" style="top:685px;width:324px;height:31px"><h2 style="top:5px">Latest Posts</h2></div>

    <div class="abs post-date" style="top:724px">Nov 17, 2016</div>
    <div class="abs cat" style="left:86px;top:724px">Learning / Thoughts</div>
    <h3 class="abs post-title" style="left:86px;top:731px;width:130px">How to See Life as an Exciting Journey</h3>
    <p class="abs post-excerpt" style="left:86px;top:756px">Yes, life can often seem to be very complicated and it’s easy to get caught up in all the difficult... Continue Reading</p>
    <div class="photo" style="left:242px;top:723px;width:117px;height:66px;background:radial-gradient(circle at 55% 60%,#9ccf6a,#4f8a33 60%,#2f5a22)" role="img" aria-label="Green leaf close-up"></div>
    <div class="abs hr" style="left:35px;top:805px;width:324px;background:#aaa"></div>

    <div class="abs post-date" style="top:814px">Nov 10, 2016</div>
    <div class="abs cat" style="left:86px;top:814px">Travel</div>
    <h3 class="abs post-title" style="left:86px;top:821px;width:130px">Travel the World and See it’s Beauty</h3>
    <p class="abs post-excerpt" style="left:86px;top:846px">Recently I had this thought that life is actually not too long and as long as one can, it’s kind... Continue Reading</p>
    <div class="photo" style="left:242px;top:813px;width:117px;height:66px;background:linear-gradient(180deg,#e5e5e2,#b9b2a8 55%,#8c8680)" role="img" aria-label="Street with a shrine gate and a small car"></div>
    <div class="abs hr" style="left:35px;top:894px;width:324px;background:#aaa"></div>

    <div class="abs post-date" style="top:903px">Oct 23, 2016</div>
    <div class="abs cat" style="left:86px;top:903px">Architecture / Travel</div>
    <h3 class="abs post-title" style="left:86px;top:910px;width:130px">Living in a Big City or a Small Town</h3>
    <p class="abs post-excerpt" style="left:86px;top:935px">I always considered me a city person and I only recently learned how it is to live in a small... Continue Reading</p>
    <div class="photo" style="left:242px;top:902px;width:117px;height:66px;background:linear-gradient(180deg,#d6d8da,#a9aeb2 55%,#6d7479)" role="img" aria-label="City skyline with tall buildings"></div>
  </section>

  <aside>
    <div class="abs hr dark" style="left:371px;top:685px;width:156px"></div>
    <div class="abs ad">
      <div class="ad-art" role="img" aria-label="Stacked diagonal colour stripes in teal, cream, red and brown"></div>
      <div class="ad-text">GET<br>TARIN<span class="ad-sub">Writer Theme</span><span style="font-size:9px">⟶</span></div>
    </div>
    <div class="abs hr dark" style="left:371px;top:792px;width:156px"></div>
    <h3 class="abs side-head" style="left:371px;top:801px">Categories</h3>
    <p class="abs side-list" style="left:371px;top:816px">Architecture / Art / Cities / eateries / Family / Food / Learning / Meditation / Nature / Photography / Society / Socitey / spotlight / stories / Thoughts / Travel / Trends / Video</p>
    <div class="abs hr dark" style="left:371px;top:867px;width:156px"></div>
    <h3 class="abs side-head" style="left:371px;top:876px">The Archives</h3>
    <p class="abs side-list" style="left:371px;top:892px">November 2016 / October 2016 / August 2016 / June 2016 / May 2016 / March 2016 / February 2016 / January 2016 / December 2015 / September 2015 / August 2015 / July 2015 / June 2015 / April 2015 / February 2015 / January 2015 / November 2014 / June 2014 / March 2014 / September 2013</p>
    <div class="abs follow">
      <h3>Follow this blog</h3>
      <p>Follow this blog and receive <b><i>notifications</i></b> of new posts by email.</p>
      <div class="field">Enter your email address</div>
      <div class="btn">FOLLOW</div>
    </div>
  </aside>

  <section>
    <div class="photo feature" role="img" aria-label="Café breakfast table with coffee and plated vegan dishes"></div>
    <div class="abs tags" style="left:35px;top:1122px"><span class="tag">Eateries</span><span class="tag">Food</span></div>
    <h2 class="abs overlay-title" style="left:35px;top:1132px;width:310px;font-size:17.5px;line-height:20px">Vegan Breakfast at one of our Favorite Cafés</h2>
    <div class="abs meta light" style="left:35px;top:1184px">By Clara Weston / Oct 19, 2016</div>
  </section>
</div>
</body>
</html>
```